quiltano

social business web site uniting communities in condominiums, clubs, hotels and the shops outlets nearby resulting in discounts coupons to the members and deal of the day offers in the vicinity of the communities.
the page can be seen at QUILTANO.COM and the logo is seen there in red and blue colors which is to be maintained.
the ultimate idea of this network is to exercise the power of the mobs when applied to any goals either commercial, social, environmental or political and give power to the mobs to let them rule.
we need 2 pages:
front page - home which is currently fixed page but in future will be dynamic with regular feeds and updates. so this condition must be foreseen in the project.
inner page - we hv many pages inside but the same construction, just titled differently.
the winning layout will have to be supplied also in html and css format.

Industry/Entity Type

Political

```html
<!DOCTYPE html>
<html lang="en">
<head>
<meta charset="utf-8">
<title>Quiltano</title>
<link href="https://fonts.googleapis.com/css2?family=Ubuntu:wght@300;400&family=Didact+Gothic&family=Crimson+Text&family=Delius&display=swap" rel="stylesheet">
<style>
:root{
  --dark:#3b3b3b;
  --dark-2:#2f2f2f;
  --blue:#1a6fd6;
  --blue-dark:#0d56b8;
  --red:#e3141a;
  --red-dark:#c10d10;
  --text:#3a3a3a;
  --muted:#777;
  --line:#d4d4d4;
  --paper:#f3f3f3;
  --banner:#dfe7ec;
  --banner-bar:#b9cfe2;
}
*{margin:0;padding:0;box-sizing:border-box}
html,body{width:1200px;height:800px;overflow:hidden}
body{position:relative;background:radial-gradient(ellipse at center,#fbfbfb 0%,var(--paper) 70%,#e9e9e9 100%);font-family:"Delius",cursive;color:var(--text)}
.abs{position:absolute}

.site-header{position:absolute;left:0;top:0;width:1200px;height:101px;background:var(--dark)}
.brand{left:230px;top:30px;display:flex;align-items:center;gap:8px}
.brand-dot{width:22px;height:22px;border-radius:50%;background:var(--blue)}
.brand-name{font-family:"Ubuntu",sans-serif;font-size:32px;color:var(--red);font-weight:400}
.contact-line{top:18px;font-family:"Didact Gothic",sans-serif;font-size:13.5px;letter-spacing:1.2px;color:#c9b7aa}
.main-nav{left:400px;top:62px;display:flex;gap:5px}
.main-nav a{display:block;height:17px;line-height:17px;text-align:center;font-family:"Didact Gothic",sans-serif;font-size:13.5px;letter-spacing:1.2px;color:#eee;text-decoration:none;background:linear-gradient(#555,#444)}
.main-nav a.current{background:linear-gradient(#3d8cf0,var(--blue-dark))}

.content-panel{left:222px;top:110px;width:755px;height:634px;background:#fff;border:1px solid #e2e2e2;border-radius:4px;box-shadow:0 0 4px rgba(0,0,0,.08)}
.hero{left:227px;top:114px;width:746px;height:183px;background:linear-gradient(90deg,#e6ecef,#d8e2e8 60%,#a6dcef)}
.hero-title{left:227px;top:135px;width:560px;height:33px;background:linear-gradient(90deg,var(--banner-bar),rgba(185,207,226,.2))}
.hero-title h1{font-family:"Ubuntu",sans-serif;font-weight:400;font-size:18px;color:#3d4650;line-height:33px;padding-left:16px}
.hero-copy{left:242px;top:188px;width:454px;font-family:"Crimson Text",serif;font-size:14.5px;line-height:21.6px;color:#2c2c2c;text-align:justify}
.hero-art{left:765px;top:140px;width:208px;height:157px;background:radial-gradient(ellipse at 60% 100%,#2a8fd0 0%,#6fc4e6 45%,rgba(166,220,239,0) 75%)}

.welcome{left:231px;top:303px;font-family:"Ubuntu",sans-serif;font-weight:400;font-size:19px;color:var(--blue)}
.welcome span{color:#e4453c}
.dotted{left:231px;top:333px;width:543px;border-top:1px dotted #bbb}
.intro{left:231px;top:338px;width:543px;font-size:11px;line-height:18.4px;text-align:justify}
.intro p+p{margin-top:18.4px}

.quote-box{left:785px;top:308px;width:183px;height:161px;border:1px solid #ddd;border-radius:3px;background:#fff}
.quote-box h2{height:24px;background:linear-gradient(#2f86ea,var(--blue-dark));color:#fff;text-align:center;font-family:"Ubuntu",sans-serif;font-weight:400;font-size:13.5px;line-height:24px;border-radius:2px 2px 0 0}
.field{position:absolute;left:8px;width:165px;height:18px;border:1px solid #c9c9c9;border-radius:3px;background:linear-gradient(#fff,#ececec);font-size:10.5px;color:#555;padding:1px 8px}
.field.msg{height:42px}
.submit{position:absolute;left:8px;top:134px;width:69px;height:19px;background:linear-gradient(#f3383c,var(--red-dark));border:1px solid #fff;box-shadow:0 0 0 1px #e5a3a3;border-radius:3px;color:#fff;font-family:"Ubuntu",sans-serif;font-size:12px;text-align:center;line-height:17px}

.feature{position:absolute;top:485px;width:236px}
.feature-bar{height:23px;border-radius:2px;color:#fff;font-family:"Ubuntu",sans-serif;font-size:14px;line-height:23px;letter-spacing:.4px;padding-left:67px}
.feature.red .feature-bar{background:linear-gradient(#f21b1f,var(--red-dark))}
.feature.blue .feature-bar{background:linear-gradient(#2d85ec,var(--blue-dark))}
.feature.dark .feature-bar{background:linear-gradient(#555,#333);padding-left:77px}
.feature-icon{position:absolute;top:-15px;left:14px;width:44px;height:44px}
.feature p{margin-top:10px;padding:0 2px;font-size:10.5px;line-height:16.8px;text-align:justify}
.read-more{position:absolute;top:106px;font-size:10.5px;color:var(--red);border-bottom:1px solid currentColor;padding-right:4px;text-decoration:none}
.feature.blue .read-more{color:var(--blue)}
.feature.dark .read-more{color:#333}

.strip{position:absolute;top:620px;width:357px;height:99px;border:1px solid #ddd;border-radius:4px;background:#fff}
.strip-label{position:absolute;left:0;top:0;width:95px;height:97px;border-right:1px solid #ddd;background:#f7f7f7;text-align:center;padding-top:22px}
.strip-label small{display:block;margin-top:4px;font-family:"Ubuntu",sans-serif;font-size:10px;color:#777}
.strip-label strong{display:block;font-family:"Ubuntu",sans-serif;font-weight:300;font-size:12.5px;color:#444}
.strip-body{position:absolute;top:14px;font-size:10.5px;line-height:15.2px;text-align:justify}
.strip-link{display:inline-block;margin-top:8px;color:var(--red);border-bottom:1px solid currentColor;font-size:10.5px;line-height:12px}
.quote-mark{position:absolute;font-family:"Crimson Text",serif;font-size:44px;color:#ddd;line-height:1}

.site-footer{position:absolute;left:0;top:744px;width:1200px;height:56px;background:var(--dark-2)}
.footer-nav{position:absolute;top:9px;width:1200px;text-align:center;font-family:"Didact Gothic",sans-serif;font-size:11.5px;letter-spacing:1px;color:#eee;word-spacing:2px}
.footer-nav span{margin:0 12px;color:#bbb}
.copyright{position:absolute;top:31px;width:1200px;text-align:center;font-family:"Didact Gothic",sans-serif;font-size:9.5px;letter-spacing:.8px;color:#aaa}
</style>
</head>
<body>

<header class="site-header">
  <div class="abs brand"><span class="brand-dot"></span><span class="brand-name">Quiltano</span></div>
  <div class="abs contact-line" style="left:623px">Phone : 555 (0199) 47</div>
  <div class="abs contact-line" style="left:791px">E-mail : info@quiltano.com</div>
  <nav class="abs main-nav">
    <a class="current" style="width:91px">Home</a>
    <a style="width:90px">About Us</a>
    <a style="width:110px">How It Work</a>
    <a style="width:110px">What Quiltz?</a>
    <a style="width:81px">Contact</a>
    <a style="width:73px">Login</a>
  </nav>
</header>

<div class="abs content-panel"></div>

<section>
  <div class="abs hero"></div>
  <div class="abs hero-art" role="img" aria-label="Illustration of a crowd standing on a globe with social message bubbles above them"></div>
  <div class="abs hero-title"><h1>Lorem Ipsum is simply dummy text of the printing</h1></div>
  <p class="abs hero-copy">Lorem Ipsum is simply dummy text of the printing and typesetting industry. Lorem Ipsum has been the industry's standard dummy text ever since the 1500s, when an unknown printer took a galley of tnic typesetting, remaining essentially unchanged.</p>
</section>

<h2 class="abs welcome" style="font-weight:400">Welcome to <span>Quiltano</span></h2>
<div class="abs dotted"></div>
<div class="abs intro">
  <p>Lorem Ipsum is simply dummy text of the printing and typesetting industry. Lorem Ipsum has been the industry's standard dummy text ever since the 1500s, when an unknown printer took a galley of type and scrambled it to make a type specimen book. It has survived not only five centuries, but also the leap into electronic typesetting, remaining essentially unchanged.</p>
  <p>It was popularised in the 1960s with the release of Tessaline sheets containing Lorem Ipsum passages, and more recently with desktop publishing software like Folio Composer including versions of Lorem Ipsum.</p>
</div>

<aside class="abs quote-box">
  <h2>Request Quote</h2>
  <div class="field" style="top:32px">Name :</div>
  <div class="field" style="top:58px">Email :</div>
  <div class="field msg" style="top:84px">Message :</div>
  <div class="submit">Submit</div>
</aside>

<div class="feature red" style="left:234px">
  <div class="feature-bar">WHAT WE DO?</div>
  <div class="feature-icon" role="img" aria-label="Illustration of a support agent" style="background:linear-gradient(#c98a3c,#333);border-radius:6px 6px 0 0"></div>
  <p>Lorem Ipsum is simply dummy text of the printing and typesetting industry. when an unknown printer took a galley of type and scrambled it to make a type specimen book.</p>
  <a class="read-more" style="left:161px">Read More »</a>
</div>
<div class="feature blue" style="left:482px">
  <div class="feature-bar" style="padding-left:99px">WHO WE ARE?</div>
  <svg class="feature-icon" viewBox="0 0 44 44" style="left:18px"><circle cx="22" cy="22" r="12" fill="#fff" stroke="#8a8a8a" stroke-width="2"/></svg>
  <p>Lorem Ipsum is simply dummy text of the printing and typesetting industry. when an unknown printer took a galley of type and scrambled it to make a type specimen book.</p>
  <a class="read-more" style="left:160px">Read More »</a>
</div>
<div class="feature dark" style="left:729px">
  <div class="feature-bar">WHY CHOOSE US?</div>
  <svg class="feature-icon" viewBox="0 0 44 44" style="left:13px"><ellipse cx="19" cy="18" rx="14" ry="11" fill="#8e8e8e"/><ellipse cx="27" cy="27" rx="12" ry="9" fill="#b5b5b5" stroke="#fff" stroke-width="2"/></svg>
  <p>Lorem Ipsum is simply dummy text of the printing and typesetting industry. when an unknown printer took a galley of type and scrambled it to make a type specimen book.</p>
  <a class="read-more" style="left:161px">Read More »</a>
</div>

<div class="strip" style="left:235px">
  <div class="strip-label">
    <svg width="26" height="20" viewBox="0 0 26 20"><ellipse cx="11" cy="8" rx="10" ry="7" fill="#a9a9a9"/><ellipse cx="17" cy="12" rx="8" ry="6" fill="#c4c4c4"/></svg>
    <small>WHAT OUR</small><strong>CLIENT SAYS</strong>
  </div>
  <span class="quote-mark" style="left:106px;top:12px">“</span>
  <span class="quote-mark" style="left:318px;top:56px">”</span>
  <div class="strip-body" style="left:135px;width:180px">Lorem Ipsum is simply dummy text of the printing and typesetting industry. when an unknown printer took specimen book.<br><span class="strip-link">The Copper Kettle</span></div>
</div>
<div class="strip" style="left:606px">
  <div class="strip-label">
    <svg width="18" height="18" viewBox="0 0 18 18"><rect x="1" y="1" width="16" height="16" rx="4" fill="#b0b0b0"/><rect x="5" y="6" width="8" height="2" fill="#fff"/><rect x="5" y="10" width="6" height="2" fill="#fff"/></svg>
    <small>OUR BLOG</small><strong>WHAT'S NEW</strong>
  </div>
  <div class="strip-body" style="left:104px;width:241px">Lorem Ipsum is simply dummy text of the s simply dummy text of the printing and typesetting industry. when an unknown printer took specimen book.<br><span class="strip-link">Lorem Ipsum</span></div>
</div>

<footer class="site-footer">
  <div class="footer-nav">Home<span>\</span>About Us<span>\</span>How it Work<span>\</span>What Quiltz?<span>\</span>Contact<span>\</span>Login<span>\</span>Privacy Policy</div>
  <div class="copyright">Copyright © 2012. Quiltano. All Right Reserved</div>
</footer>

</body>
</html>
```